Our architectural studio needs a new business card

We need a business card design for our studio based in Waterloo in Belgium. We are active in architecture, design and installation.
Our works are contemporary and minimalist. our clients are refined and cultured.
Our business card must be minimalist and refined.

Project Deadline Extended
Reason: Some designers have accepted my invitation but they don't have all replied. I want to give them a chance to make one proposal. Paul

Target Market(s)

architecture

Industry/Entity Type

Business

Contact Information for Business Card

studio: paul dornevaux studio
paul dornevaux, architecte
M. +32 471 586 927
F. +322 619 4850
www.pauldornevaux-example.com
paul@pauldornevaux-example.com
14 rue des Marronniers
1420 Waterloo
Belgium

Font styles to use
Sans Serif

Requirements
Must have
• simple, minimalist, clear, elegant and chic! Black and white
Nice to have
• embossed logo, other format like a square for example
Should not have
• color, fantasy, curves, ...

```html
<!DOCTYPE html>
<html lang="fr">
<head>
<meta charset="utf-8">
<title>Paul Dornevaux Studio — Business Card</title>
<link href="https://fonts.googleapis.com/css2?family=Mulish:wght@300;400;800&display=swap" rel="stylesheet">
<style>
  :root {
    --backdrop: #f3f3f3;
    --card: #ffffff;
    --ink: #1c1c1c;
    --ink-soft: #3a3a3a;
    --edge: #1c1c1c;
  }
  * { margin: 0; padding: 0; box-sizing: border-box; }
  html, body {
    width: 1200px; height: 800px; overflow: hidden;
    background: var(--backdrop);
    font-family: "Mulish", sans-serif;
    color: var(--ink);
  }
  .sheet {
    width: 1200px; height: 800px;
    display: flex; align-items: center; justify-content: center; gap: 60px;
  }
  .card {
    position: relative;
    width: 510px; height: 320px;
    background: var(--card);
    border-bottom: 3px solid var(--edge);
    box-shadow: 0 2px 10px rgba(0,0,0,0.08);
  }

  /* Front */
  .card-front .mark {
    position: absolute; left: 0; right: 0; top: 80px;
    display: flex; align-items: center; justify-content: center; gap: 14px;
  }
  .mark-square { width: 34px; height: 34px; background: var(--ink); }
  .mark-name {
    font-weight: 800; font-size: 26px; letter-spacing: 0.02em; color: var(--ink);
  }
  .card-front .studio-name {
    position: absolute; left: 0; right: 0; bottom: 70px;
    text-align: center;
    font-weight: 800; font-size: 13px; letter-spacing: 0.32em; text-transform: uppercase;
  }

  /* Back */
  .card-back .header {
    position: absolute; left: 48px; right: 40px; top: 36px;
    display: flex; align-items: flex-start; gap: 16px;
  }
  .person { flex: none; }
  .person-name {
    font-weight: 300; font-size: 26px; letter-spacing: 0.02em; text-transform: uppercase; line-height: 1;
    white-space: nowrap;
  }
  .person-role { font-weight: 300; font-size: 13px; margin-top: 4px; color: var(--ink-soft); }
  .header .rule-top {
    flex: 1; height: 1px; margin-top: 22px; background: var(--ink-soft);
  }
  .contacts {
    position: absolute; left: 48px; top: 122px;
    display: grid; grid-template-columns: 72px auto; row-gap: 2px;
    font-weight: 300; font-size: 14px; color: var(--ink-soft); text-transform: uppercase;
    white-space: nowrap;
  }
  .card-back .rule-mid {
    position: absolute; left: 48px; top: 205px; width: 300px; height: 1px; background: var(--ink-soft);
  }
  .address {
    position: absolute; left: 48px; top: 218px;
    font-weight: 300; font-size: 13px; line-height: 1.6; color: var(--ink-soft);
    white-space: nowrap;
  }
  .address strong { font-weight: 800; }
</style>
</head>
<body>
<main class="sheet">
  <section class="card card-front" aria-label="Recto">
    <div class="mark">
      <span class="mark-square"></span>
      <span class="mark-name">PDS</span>
    </div>
    <p class="studio-name">Paul Dornevaux Studio</p>
  </section>

  <section class="card card-back" aria-label="Verso">
    <div class="header">
      <div class="person">
        <p class="person-name">Paul Dornevaux</p>
        <p class="person-role">Architecte</p>
      </div>
      <span class="rule-top"></span>
    </div>
    <dl class="contacts">
      <dt>Mobile</dt><dd>+32 471 586 927</dd>
      <dt>Fax</dt><dd>+322 619 4850</dd>
      <dt>Email</dt><dd>paul@pauldornevaux-example.com</dd>
    </dl>
    <span class="rule-mid"></span>
    <p class="address">
      14 rue des Marronniers 1420 Waterloo Belgium<br>
      www.<strong>pauldornevaux-example</strong>.com
    </p>
  </section>
</main>
</body>
</html>
```